Gift voucher for a photo shoot, folding card DIN long (21 x 9.8 cm)

Hello, I'm a professional photographer and need a new design for my gift voucher card for a photo shoot. The design should be applicable to all types of photo shoots (neutral). I prefer a sophisticated design. The folded card should be printed on both sides.
My data should be included: Logo, Address: Wendtholzer Strße 27, 07549 Gera, Email: fotograf@malteburgardt.eu, Website: www.malteburgardt.eu Tel.: 0173 / 4958302
Updates

Please design the folding card in DIN long format (105 x 210 mm, landscape format). The card should open horizontally. Please design the front with the words "Gift voucher for you" and my logo. Please make the logo small – the words "Gift voucher" should be in the foreground.
The colors - use elegant gray with gold or white font color.
The inside should contain the words: Photo shoot for ........ worth .....€, as well as my logo.
My contact details should be on the back.

Target Market(s)

Private customer

Colors

Designer to choose only greyscale colors for use in the design.

Requirements
Must have
• Noble appearance, a gift voucher that one likes to give away, words: Gift voucher for you, photo shoot for ..., worth .......€
Nice to have
• Noble appearance of the gift voucher, a gift voucher that you like to give away
Should not have
• no pictures

```html
<!DOCTYPE html>
<html lang="en">
<head>
<meta charset="utf-8">
<title>Gift Voucher – Malte Burgardt</title>
<link href="https://fonts.googleapis.com/css2?family=Cinzel:wght@400&family=Great+Vibes&family=Tenor+Sans&family=Tinos:ital,wght@0,400;0,700;1,400&display=swap" rel="stylesheet">
<style>
  :root {
    --backdrop: #000000;
    --card: #eff0f1;
    --ink: #1a1a1a;
    --gold-light: #f6dc9a;
    --gold: #d9ad55;
    --gold-deep: #b8862f;
  }
  * { margin: 0; padding: 0; box-sizing: border-box; }
  html, body { width: 838px; height: 1200px; overflow: hidden; background: var(--backdrop); }
  .sheet { position: relative; width: 838px; height: 1200px; }
  .card {
    position: absolute; left: 182px; width: 476px; height: 238px;
    background: var(--card); color: var(--ink);
  }
  .card--front { top: 210px; }
  .card--inside { top: 481px; }
  .card--back { top: 751px; }

  .brand { position: absolute; left: 0; width: 100%; text-align: center; }
  .brand__mark {
    position: absolute; left: 50%; transform: translateX(-50%);
    border: 1.6px solid var(--ink); border-radius: 50%;
  }
  .brand__name {
    position: absolute; left: 0; width: 100%; text-align: center;
    font-family: "Cinzel", serif; font-weight: 400; color: var(--ink); white-space: nowrap;
  }
  .card--front .brand__mark { top: 44px; width: 32px; height: 32px; }
  .card--front .brand__name { top: 78px; font-size: 17px; }
  .card--inside .brand__mark,
  .card--back .brand__mark { width: 44px; height: 44px; }
  .card--inside .brand__mark { top: 26px; }
  .card--back .brand__mark { top: 21px; }
  .card--inside .brand__name,
  .card--back .brand__name { font-size: 22px; }
  .card--inside .brand__name { top: 74px; }
  .card--back .brand__name { top: 69px; }

  .rule {
    position: absolute; left: 68px; width: 341px; top: 112px; height: 1.5px;
    background: linear-gradient(90deg, rgba(217,173,85,0.1), var(--gold) 18%, var(--gold-light) 50%, var(--gold) 82%, rgba(217,173,85,0.1));
  }
  .card--inside .rule { top: 118px; }
  .card--back .rule { top: 112px; }

  .gold-text {
    background: linear-gradient(100deg, var(--gold-deep), var(--gold-light) 45%, var(--gold) 70%, var(--gold-light));
    -webkit-background-clip: text; background-clip: text; color: transparent;
  }
  .voucher-title {
    position: absolute; top: 124px; left: 0; width: 100%; text-align: center;
    font-family: "Cinzel", serif; font-weight: 400; font-size: 37px; letter-spacing: 5px; line-height: 1; white-space: nowrap;
  }
  .voucher-subtitle {
    position: absolute; top: 166px; left: 0; width: 100%; text-align: center;
    font-family: "Great Vibes", cursive; font-size: 30px; line-height: 1;
  }

  .voucher-line {
    position: absolute; left: 34px; top: 183px;
    font-family: "Tenor Sans", sans-serif; font-size: 15px; letter-spacing: -0.3px; white-space: nowrap;
    display: flex; align-items: baseline;
  }
  .voucher-line__blank {
    display: inline-block; border-bottom: 1px dotted var(--ink); margin: 0 5px;
  }
  .voucher-line__blank--name { width: 123px; }
  .voucher-line__blank--amount { width: 48px; margin-right: 0; }

  .contact { position: absolute; left: 108px; top: 124px; line-height: 1; font-style: normal; }
  .contact__item { position: absolute; left: 0; white-space: nowrap; font-style: normal; }
  .contact__address { top: 0; font-family: "Tenor Sans", sans-serif; font-size: 14.5px; text-transform: uppercase; letter-spacing: -0.4px; }
  .contact__email { top: 24px; font-family: "Tinos", serif; font-style: italic; font-size: 15px; }
  .contact__web { top: 46px; font-family: "Tinos", serif; font-size: 14.5px; letter-spacing: 1.3px; }
  .contact__phone { top: 68px; font-family: "Tinos", serif; font-weight: 700; font-size: 14.5px; letter-spacing: 1.8px; }
</style>
</head>
<body>
<main class="sheet">

  <section class="card card--front" aria-label="Front of the voucher">
    <div class="brand">
      <span class="brand__mark"></span>
      <span class="brand__name">Malte Burgardt</span>
    </div>
    <div class="rule"></div>
    <h1 class="voucher-title gold-text">GIFT VOUCHER</h1>
    <p class="voucher-subtitle gold-text">for you</p>
  </section>

  <section class="card card--inside" aria-label="Inside of the voucher">
    <div class="brand">
      <span class="brand__mark"></span>
      <span class="brand__name">Malte Burgardt</span>
    </div>
    <div class="rule"></div>
    <p class="voucher-line">
      PHOTO SHOOT FOR<span class="voucher-line__blank voucher-line__blank--name"></span>WORTH<span class="voucher-line__blank voucher-line__blank--amount"></span>€
    </p>
  </section>

  <section class="card card--back" aria-label="Back of the voucher">
    <div class="brand">
      <span class="brand__mark"></span>
      <span class="brand__name">Malte Burgardt</span>
    </div>
    <div class="rule"></div>
    <address class="contact">
      <span class="contact__item contact__address">Wendtholzer Strße 27, 07549 Haldenfurt,</span>
      <span class="contact__item contact__email">fotograf@malteburgardt.eu</span>
      <span class="contact__item contact__web">www.malteburgardt.eu</span>
      <span class="contact__item contact__phone">0173 / 4958302</span>
    </address>
  </section>

</main>
</body>
</html>
```